Email graphic design for a survey

We have built a survey on Formly Nest and require someone who can develop some graphics in the email that will be sent in the first instance.
Target: Australia Wide, A
Offer: Opportunity to win 3 hours of one-to-one career coaching to responders as a prize draw
Email Creative Recommendations:
• A good text to image ratio
• Simple, but effective image based email which outlines both the inclusions of the survey and the one-to-one coaching prize
• Mobile and tablet responsive
• Refer to attached examples for one of our clients - Copper Lane Surveys
Landing Page: As supplied - https://www.formlynest.com/r/brindlewick Mobile and tablet responsive
Thank you for your submissions
Target Market(s)
ages 25-60 years old, white collar workers targeted
Other font styles liked:
- ubuntu

```html
<!DOCTYPE html>
<html lang="en">
<head>
<meta charset="utf-8">
<title>Brindlewick – Win Career Coaching</title>
<link rel="stylesheet" href="https://fonts.googleapis.com/css2?family=Ubuntu:ital,wght@0,400;0,500;0,700;1,400&display=swap">
<style>
  :root {
    --blue-light: #19a6e2;
    --blue-deep: #0650c0;
    --ink: #2f3b48;
    --text: #3a4450;
    --orange-light: #ffa45e;
    --orange: #ff7318;
    --cream: #f7f7f2;
    --white: #ffffff;
    --dot-grey: #b9bcc0;
  }
  * { box-sizing: border-box; margin: 0; padding: 0; }
  html, body { width: 1200px; height: 3204px; overflow: hidden; }
  body {
    position: relative;
    background: var(--white);
    font-family: "Ubuntu", sans-serif;
    color: var(--text);
  }
  .layer { position: absolute; left: 0; top: 0; }
  .hero-photo {
    position: absolute; left: 0; top: 0; width: 1200px; height: 840px;
    background:
      radial-gradient(ellipse 520px 300px at 560px 620px, #5d86a6 0%, rgba(93,134,166,0) 100%),
      radial-gradient(ellipse 260px 220px at 860px 560px, #4f7898 0%, rgba(79,120,152,0) 100%),
      radial-gradient(ellipse 260px 220px at 340px 600px, #5a82a2 0%, rgba(90,130,162,0) 100%),
      linear-gradient(180deg, #6fb6e3 0%, #9fd2ee 45%, #80b6d8 100%);
  }
  .doodle-spot {
    position: absolute; left: 330px; top: 1416px; width: 170px; height: 124px;
    border-radius: 40px; background: rgba(255, 115, 24, 0.14);
  }
  .brand {
    position: absolute; left: 0; width: 1200px; text-align: center;
    font-weight: 500; font-size: 38px; color: var(--ink); letter-spacing: 1px;
  }
  .brand-top { top: 30px; }
  .brand-foot { top: 2970px; }
  .brand .mark {
    display: inline-block; width: 14px; height: 14px; border-radius: 50%;
    background: var(--ink); margin-right: 10px; vertical-align: middle;
  }
  .headline {
    position: absolute; top: 266px; left: 0; width: 1200px; text-align: center;
    font-weight: 700; font-size: 42px; line-height: 52px; letter-spacing: 2px;
    color: var(--white);
  }
  .headline .dark { color: var(--ink); }
  .btn {
    position: absolute; left: 470px; width: 260px; height: 70px;
    border-radius: 22px;
    background: linear-gradient(90deg, var(--orange-light), var(--orange));
    box-shadow: 0 8px 16px rgba(255, 115, 24, 0.3);
    color: var(--white); font-weight: 700; font-size: 24px; letter-spacing: 1px;
    line-height: 70px; text-align: center; text-decoration: none;
  }
  .btn-hero { top: 414px; }
  .btn-intro { top: 1214px; }
  .btn-close { top: 2664px; }
  .greeting {
    position: absolute; top: 896px; left: 0; width: 1200px; text-align: center;
    font-size: 28px; letter-spacing: 0.5px;
  }
  .intro {
    position: absolute; top: 988px; left: 110px; width: 980px; text-align: center;
    font-size: 28px; line-height: 48px; letter-spacing: 1px;
  }
  strong { font-weight: 700; color: var(--ink); }
  .section-title {
    position: absolute; top: 1334px; left: 0; width: 1200px; text-align: center;
    font-weight: 700; font-size: 42px; letter-spacing: 2px; color: var(--ink);
  }
  .step-num {
    position: absolute; font-weight: 700; font-size: 100px; line-height: 100px; color: var(--ink);
  }
  .step-label {
    position: absolute; font-size: 28px; line-height: 34px; letter-spacing: 1px;
  }
  .closing-title {
    position: absolute; top: 2490px; left: 0; width: 1200px; text-align: center;
    font-weight: 700; font-size: 44px; letter-spacing: 1px; color: var(--ink);
  }
  .closing-text {
    position: absolute; top: 2560px; left: 0; width: 1200px; text-align: center;
    font-size: 28px; line-height: 34px; letter-spacing: 1px;
  }
  .contact {
    position: absolute; left: 0; width: 1200px; text-align: center;
    color: var(--white); font-size: 24px; font-weight: 500;
  }
  .contact svg { vertical-align: middle; margin-right: 10px; }
  .contact-email { top: 3042px; }
  .contact-phone { top: 3088px; }
</style>
</head>
<body>

  <div class="hero-photo" role="img" aria-label="Photo area: three excited young people jumping with arms raised against a blue sky, tinted blue"></div>

  <svg class="layer" width="1200" height="3204" viewBox="0 0 1200 3204" aria-hidden="true">
    <defs>
      <linearGradient id="brandBlue" x1="0" y1="0" x2="1" y2="0">
        <stop offset="0" stop-color="#19a6e2"/>
        <stop offset="1" stop-color="#0650c0"/>
      </linearGradient>
      <linearGradient id="iconOrange" x1="0" y1="0" x2="1" y2="1">
        <stop offset="0" stop-color="#ffa45e"/>
        <stop offset="1" stop-color="#ff7318"/>
      </linearGradient>
      <filter id="softShadow" x="-30%" y="-30%" width="160%" height="160%">
        <feDropShadow dx="0" dy="6" stdDeviation="8" flood-color="#000" flood-opacity="0.12"/>
      </filter>
    </defs>

    <path d="M0 0 H1200 V70 C1130 150 1020 60 920 110 C800 170 720 40 580 90 C440 140 360 200 230 150 C140 115 70 100 0 120 Z" fill="url(#brandBlue)"/>

    <rect x="0" y="1200" width="1200" height="1210" fill="var(--cream)"/>

    <path d="M0 830 C70 700 260 620 400 690 C520 750 580 830 710 770 C860 690 1010 560 1200 610 V1330 Q600 1670 0 1330 Z" fill="var(--white)" filter="url(#softShadow)"/>
    <path d="M0 840 C70 710 260 630 400 700 C520 760 580 840 710 780 C860 700 1010 570 1200 620 V1320 Q600 1660 0 1320 Z" fill="var(--white)"/>

    <path d="M318 1620 L572 1752" fill="none" stroke="var(--dot-grey)" stroke-width="4" stroke-dasharray="2 12" stroke-linecap="round"/>
    <path d="M676 1850 C720 1940 720 2060 600 2110 C540 2132 500 2136 450 2136" fill="none" stroke="var(--ink)" stroke-width="5" stroke-dasharray="1 13" stroke-linecap="round"/>

    <circle cx="246" cy="1574" r="66" fill="var(--white)" filter="url(#softShadow)"/>
    <circle cx="636" cy="1786" r="66" fill="var(--white)" filter="url(#softShadow)"/>
    <circle cx="370" cy="2112" r="66" fill="url(#iconOrange)" filter="url(#softShadow)"/>

    <g fill="none" stroke="var(--orange)" stroke-width="3.5" stroke-linejoin="round">
      <g transform="translate(246 1574)">
        <rect x="-26" y="-14" width="52" height="14"/><rect x="-22" y="0" width="44" height="30"/>
        <line x1="0" y1="-14" x2="0" y2="30"/><line x1="-22" y1="14" x2="22" y2="14"/>
        <circle cx="-8" cy="-22" r="7"/><circle cx="8" cy="-22" r="7"/>
      </g>
      <g transform="translate(636 1786)">
        <rect x="-26" y="-14" width="52" height="14"/><rect x="-22" y="0" width="44" height="30"/>
        <line x1="0" y1="-14" x2="0" y2="30"/><line x1="-22" y1="14" x2="22" y2="14"/>
        <circle cx="-8" cy="-22" r="7"/><circle cx="8" cy="-22" r="7"/>
      </g>
      <g transform="translate(370 2112)" stroke="var(--white)">
        <rect x="-26" y="-14" width="52" height="14"/><rect x="-22" y="0" width="44" height="30"/>
        <line x1="0" y1="-14" x2="0" y2="30"/><line x1="-22" y1="14" x2="22" y2="14"/>
        <circle cx="-8" cy="-22" r="7"/><circle cx="8" cy="-22" r="7"/>
      </g>
    </g>

    <path d="M0 2900 C100 2840 210 2830 320 2880 C420 2925 490 2790 620 2770 C760 2750 820 2870 960 2830 C1070 2800 1110 2700 1200 2700 V3204 H0 Z" fill="url(#brandBlue)"/>
  </svg>

  <div class="doodle-spot" role="img" aria-label="Hand-drawn orange squiggle arrow pointing to step one"></div>

  <div class="brand brand-top"><span class="mark"></span>brindlewick</div>

  <h1 class="headline">READY TO WIN 3 HOURS OF <span class="dark">ONE ON ONE</span><br><span class="dark">CAREER COACHING?</span></h1>
  <a class="btn btn-hero" href="https://www.formlynest.com/r/brindlewick">GET STARTED</a>

  <p class="greeting">Hi <em>(First Name)</em>,</p>
  <p class="intro">We are interested in getting your thoughts on professional<br>development as your input will shape how organisations are<br>supporting their people through change. You have the <strong>opportunity<br>to win</strong> one of our <strong>3 hour one on one career coaching sessions!!!</strong></p>
  <a class="btn btn-intro" href="https://www.formlynest.com/r/brindlewick">GET STARTED</a>

  <h2 class="section-title">THIS IS HOW EASY IT IS</h2>

  <span class="step-num" style="left:150px; top:1664px;">1</span>
  <p class="step-label" style="left:208px; top:1686px;">Sign Up to<br><strong>Brindlewick</strong> Surveys</p>

  <span class="step-num" style="left:740px; top:1744px;">2</span>
  <p class="step-label" style="left:820px; top:1766px; text-align:center;">Start Completing<br>Surveys</p>

  <span class="step-num" style="left:154px; top:2212px;">3</span>
  <p class="step-label" style="left:224px; top:2218px; text-align:center;">Your opportunity to win<br><strong>one on one career<br>coaching</strong></p>

  <h2 class="closing-title">What are you waiting for?</h2>
  <p class="closing-text">Register today and win a <strong>one on one<br>career coaching!</strong></p>
  <a class="btn btn-close" href="https://www.formlynest.com/r/brindlewick">GET STARTED</a>

  <div class="brand brand-foot"><span class="mark"></span>brindlewick</div>
  <p class="contact contact-email">
    <svg width="28" height="20" viewBox="0 0 28 20" aria-hidden="true"><rect x="1" y="1" width="26" height="18" fill="none" stroke="#fff" stroke-width="2"/><path d="M1 1 L14 11 L27 1" fill="none" stroke="#fff" stroke-width="2"/></svg>enquiries@brindlewick.co
  </p>
  <p class="contact contact-phone">
    <svg width="22" height="22" viewBox="0 0 24 24" aria-hidden="true"><path d="M6.6 10.8a15 15 0 0 0 6.6 6.6l2.2-2.2a1 1 0 0 1 1-.25 11.4 11.4 0 0 0 3.6.57 1 1 0 0 1 1 1V20a1 1 0 0 1-1 1A17 17 0 0 1 3 4a1 1 0 0 1 1-1h3.5a1 1 0 0 1 1 1c0 1.25.2 2.45.57 3.57a1 1 0 0 1-.25 1z" fill="#fff"/></svg>61 255501734
  </p>

</body>
</html>
```